Visitenkarten-Design für Persisches Restaurant
Zielgruppe
persisches Restaurant, suche ein Hochwertiges Design für internationale Kunden
Aufgabenstellung
möchte eine hochwertige und elegante visitenkarte
auf der Vorderseite sollte das Logo sein und auf der Rückseite Öffnungszeit, Adresse, Tel. E-Mail und homepage

```html
<!DOCTYPE html>
<html lang="de">
<head>
<meta charset="utf-8">
<title>Golnar – Visitenkarten</title>
<link rel="stylesheet" href="https://fonts.googleapis.com/css2?family=Kreon:wght@400;500;600&family=Open+Sans:wght@400&display=swap">
<style>
  :root {
    --page: #ffffff;
    --card: #ffffff;
    --gold: #b8934f;
    --gold-text: #7a5a2e;
    --slate: #6d6e70;
    --slate-text: #6f6f6f;
    --logo-dark: #2b2b2b;
    --band-text: #ffffff;
  }
  html, body {
    margin: 0;
    padding: 0;
    width: 1200px;
    height: 2338px;
    overflow: hidden;
    background: var(--page);
  }
  .sheet {
    position: relative;
    width: 1200px;
    height: 2338px;
  }
  .card {
    position: absolute;
    width: 277px;
    height: 498px;
    background: var(--card);
    box-shadow: 0 4px 14px rgba(0,0,0,0.28), 0 1px 3px rgba(0,0,0,0.18);
    overflow: hidden;
  }
  .card--front {
    display: flex;
    align-items: center;
    justify-content: center;
  }
  .wordmark {
    font-family: "Kreon", Georgia, serif;
    font-weight: 500;
    font-size: 42px;
    letter-spacing: 1px;
    line-height: 1;
    margin-top: -56px;
  }
  .theme-gold .wordmark { color: var(--gold); }
  .theme-slate .wordmark { color: var(--logo-dark); }

  .contact {
    position: absolute;
    top: 62px;
    left: 0;
    width: 100%;
    text-align: center;
    font-size: 14px;
    line-height: 19px;
  }
  .contact .name {
    font-family: "Kreon", Georgia, serif;
    font-size: 15.5px;
  }
  .contact .detail {
    font-family: "Open Sans", Arial, sans-serif;
  }
  .contact .address { margin-top: 20px; }
  .theme-gold .contact { color: var(--gold-text); }
  .theme-slate .contact { color: var(--slate-text); }

  .hours {
    position: absolute;
    left: 0;
    bottom: 0;
    width: 100%;
    height: 231px;
  }
  .theme-gold .hours { background: var(--gold); }
  .theme-slate .hours { background: var(--slate); }
  .hours__title {
    margin: 0;
    height: 36px;
    line-height: 40px;
    text-align: center;
    font-family: "Kreon", Georgia, serif;
    font-weight: 600;
    font-size: 17px;
    color: var(--band-text);
    border-bottom: 1.5px solid rgba(255,255,255,0.9);
  }
  .hours__table {
    margin: 24px 0 0 38px;
    border-collapse: collapse;
    font-family: "Open Sans", Arial, sans-serif;
    font-size: 14px;
    color: var(--band-text);
  }
  .hours__table td {
    padding: 0;
    height: 19px;
    line-height: 19px;
    white-space: nowrap;
  }
  .hours__table .day { width: 98px; }
</style>
</head>
<body>
<main class="sheet">

  <!-- Gold edition -->
  <section class="card card--front theme-gold" style="left:265px; top:175px;">
    <div class="wordmark">Golnar</div>
  </section>

  <section class="card card--back theme-gold" style="left:644px; top:172px;">
    <div class="contact">
      <div class="name">Golnar</div>
      <div class="name">Persisches Restaurant</div>
      <div class="detail">T 069 / 48 21 90</div>
      <div class="detail">www.golnar-restaurant.de</div>
      <div class="detail address">Lindenweg 14</div>
      <div class="detail">60322 Frankfurt am Main</div>
    </div>
    <div class="hours">
      <h2 class="hours__title">Öffnungszeiten</h2>
      <table class="hours__table">
        <tr><td class="day">Montag</td><td>11:30-22:30 Uhr</td></tr>
        <tr><td class="day">Dienstag</td><td>11:30-22:30 Uhr</td></tr>
        <tr><td class="day">Mittwoch</td><td>11:30-22:30 Uhr</td></tr>
        <tr><td class="day">Donnerstag</td><td>11:30-22:30 Uhr</td></tr>
        <tr><td class="day">Freitag</td><td>11:30-22:30 Uhr</td></tr>
        <tr><td class="day">Samstag</td><td>12:00-22:30 Uhr</td></tr>
        <tr><td class="day">Sonntag</td><td>12:00-22:30 Uhr</td></tr>
      </table>
    </div>
  </section>

  <!-- Slate edition -->
  <section class="card card--front theme-slate" style="left:285px; top:1758px;">
    <div class="wordmark">Golnar</div>
  </section>

  <section class="card card--back theme-slate" style="left:644px; top:1758px;">
    <div class="contact">
      <div class="name">Golnar</div>
      <div class="name">Persisches Restaurant</div>
      <div class="detail">T 069 / 48 21 90</div>
      <div class="detail">www.golnar-restaurant.de</div>
      <div class="detail address">Lindenweg 14</div>
      <div class="detail">60322 Frankfurt am Main</div>
    </div>
    <div class="hours">
      <h2 class="hours__title">Öffnungszeiten</h2>
      <table class="hours__table">
        <tr><td class="day">Montag</td><td>11:30-22:30 Uhr</td></tr>
        <tr><td class="day">Dienstag</td><td>11:30-22:30 Uhr</td></tr>
        <tr><td class="day">Mittwoch</td><td>11:30-22:30 Uhr</td></tr>
        <tr><td class="day">Donnerstag</td><td>11:30-22:30 Uhr</td></tr>
        <tr><td class="day">Freitag</td><td>11:30-22:30 Uhr</td></tr>
        <tr><td class="day">Samstag</td><td>12:00-22:30 Uhr</td></tr>
        <tr><td class="day">Sonntag</td><td>12:00-22:30 Uhr</td></tr>
      </table>
    </div>
  </section>

</main>
</body>
</html>
```